Business Card design for Founder and CEO of new shoe company

I am looking for a business card design for my new shoe company called Strapwell.

I am launching the company this April. Strapwell shoes offers slip-on athletic and casual style shoes for men and women. The unique selling point of the brand is that all of our shoe exist without shoelaces. I have included a link to the website to offer additional information about the company, see product images, and gain inspiration for the design. You can use the store owner password "Strapwell" to access the website.

www.Strapwell.example

Thanks,
Dan Hollis

Target Market(s)

Active Men and Women ages 16-45

Industry/Entity Type

Business

Contact Information for Business Card

Dan Hollis
Founder and CEO
www.Strapwell.example
danhollis@Strapwell.example
888-555-0187 / 888-5STRAPW
Strapwell, LLC
2284 N Tamsin Ave
Chicago, IL 60699

Requirements
Must have
• Be able to quickly and easily tell that Strapwell is a shoe company from the business card

```html
<!DOCTYPE html>
<html lang="en">
<head>
<meta charset="utf-8">
<title>Strapwell Business Card</title>
<link rel="stylesheet" href="https://fonts.googleapis.com/css2?family=Open+Sans:wght@400;700&display=swap">
<style>
  :root {
    --backdrop: #e9e9eb;
    --card: #ffffff;
    --ink: #1a1a1a;
    --ink-soft: #2b2b2b;
    --shoe-pink: #d9479a;
    --shoe-blue: #4a5fc0;
    --shoe-sky: #35b4e0;
    --shoe-sky-light: #bfe6f4;
    --cap-white: #f4f4f4;
    --cap-grey: #dedede;
    --sole-dark: #2a2a2a;
    --shadow: rgba(0, 0, 0, 0.12);
  }
  * { margin: 0; padding: 0; box-sizing: border-box; }
  html, body {
    width: 1200px;
    height: 900px;
    overflow: hidden;
    background: var(--backdrop);
    font-family: "Open Sans", Arial, sans-serif;
    color: var(--ink);
  }
  .canvas {
    position: relative;
    width: 1200px;
    height: 900px;
  }
  .card {
    position: absolute;
    background: var(--card);
    box-shadow: 0 6px 22px var(--shadow);
  }
  .card-front {
    left: 238px;
    top: 60px;
    width: 555px;
    height: 345px;
  }
  .card-back {
    left: 457px;
    top: 517px;
    width: 560px;
    height: 345px;
    display: flex;
    align-items: center;
    justify-content: center;
  }
  .holder {
    position: absolute;
    right: 295px;
    top: 54px;
    text-align: right;
  }
  .holder-name {
    font-size: 18px;
    font-weight: 700;
    line-height: 24px;
  }
  .holder-title {
    font-size: 14px;
    line-height: 20px;
    color: var(--ink-soft);
  }
  .contact-list {
    position: absolute;
    left: 287px;
    top: 34px;
    list-style: none;
  }
  .contact-item {
    display: flex;
    align-items: center;
    height: 20px;
    font-size: 14px;
    color: var(--ink-soft);
  }
  .contact-icon {
    width: 11px;
    height: 11px;
    margin-right: 10px;
    fill: var(--ink);
    flex: none;
  }
  .product-photo {
    position: absolute;
    left: 47px;
    top: 165px;
    width: 463px;
    height: 130px;
    background:
      linear-gradient(180deg, transparent 0%, transparent 72%, rgba(42,42,42,0.55) 80%, rgba(255,255,255,0) 100%),
      linear-gradient(90deg,
        var(--shoe-blue) 0%,
        var(--shoe-pink) 12%,
        var(--shoe-blue) 22%,
        var(--shoe-pink) 30%,
        var(--shoe-blue) 37%,
        var(--cap-grey) 41%,
        var(--cap-white) 50%,
        var(--cap-grey) 58%,
        var(--shoe-sky) 63%,
        var(--shoe-sky-light) 72%,
        var(--shoe-sky) 80%,
        var(--shoe-sky-light) 89%,
        var(--shoe-sky) 100%);
    -webkit-mask-image: linear-gradient(180deg, rgba(0,0,0,0) 0%, #000 18%, #000 86%, rgba(0,0,0,0) 100%);
    mask-image: linear-gradient(180deg, rgba(0,0,0,0) 0%, #000 18%, #000 86%, rgba(0,0,0,0) 100%);
    border-radius: 10px;
  }
  .address {
    position: absolute;
    left: 0;
    right: 0;
    top: 307px;
    text-align: center;
    font-size: 14.5px;
    color: var(--ink-soft);
  }
  .brand-name {
    font-size: 66px;
    font-weight: 400;
    letter-spacing: 1px;
    color: var(--ink);
    line-height: 1;
  }
</style>
</head>
<body>
<main class="canvas">
  <section class="card card-front">
    <div class="holder">
      <p class="holder-name">Dan Hollis</p>
      <p class="holder-title">Founder and CEO</p>
    </div>
    <ul class="contact-list">
      <li class="contact-item">
        <svg class="contact-icon" viewBox="0 0 24 24" aria-hidden="true"><path d="M6.6 10.8c1.4 2.8 3.8 5.1 6.6 6.6l2.2-2.2c.3-.3.7-.4 1-.2 1.1.4 2.3.6 3.6.6.6 0 1 .4 1 1V20c0 .6-.4 1-1 1C10.6 21 3 13.4 3 4c0-.6.4-1 1-1h3.5c.6 0 1 .4 1 1 0 1.3.2 2.5.6 3.6.1.3 0 .7-.2 1z"/></svg>
        888-555-0187
      </li>
      <li class="contact-item">
        <svg class="contact-icon" viewBox="0 0 24 24" aria-hidden="true"><path d="M6.6 10.8c1.4 2.8 3.8 5.1 6.6 6.6l2.2-2.2c.3-.3.7-.4 1-.2 1.1.4 2.3.6 3.6.6.6 0 1 .4 1 1V20c0 .6-.4 1-1 1C10.6 21 3 13.4 3 4c0-.6.4-1 1-1h3.5c.6 0 1 .4 1 1 0 1.3.2 2.5.6 3.6.1.3 0 .7-.2 1z"/></svg>
        888-5STRAPW
      </li>
      <li class="contact-item">
        <svg class="contact-icon" viewBox="0 0 24 24" aria-hidden="true"><path d="M3 6h18v12H3z M3 6l9 7 9-7" fill="none" stroke="#1a1a1a" stroke-width="2.4"/></svg>
        danhollis@Strapwell.example
      </li>
      <li class="contact-item">
        <svg class="contact-icon" viewBox="0 0 24 24" aria-hidden="true"><circle cx="12" cy="12" r="10"/><path d="M2 12h20M12 2c3 3 3 17 0 20M12 2c-3 3-3 17 0 20" fill="none" stroke="#ffffff" stroke-width="1.6"/></svg>
        www.Strapwell.example
      </li>
    </ul>
    <div class="product-photo" role="img" aria-label="Product photo of Strapwell footwear: a pair of pink and blue slip-on sneakers, a white cap in the middle, and a pair of sky-blue athletic shoes, lined up on white"></div>
    <p class="address">Strapwell, LLC 2284 N Tamsin Ave Chicago, IL 60699</p>
  </section>

  <section class="card card-back">
    <p class="brand-name">Strapwell</p>
  </section>
</main>
</body>
</html>
```